Website/Logo Design

We need a logo and website design for an opinion mining startup called VantroLux. Our technology mines the web to automatically discover what people are saying about brands, products, etc. The project we are fielding here is for our informational, public-facing website. In its initial incarnation, it will simply be a vehicle for marketing materials and information on our company and its offerings, but it should be flexible enough to expand as more content/functionality is added.

Some designs we like are:
http://www.brivel-nodo.com
http://www.tarnwisp.com
http://www.kvh.com
http://www.zellmorit.com
http://quontavel.com
http://marbiquex.com
http://www.vadup.com
Updates

All, please try to shy away from using a photo of a person as the focal point of the design.  Our company is more technological than social.

Target Market(s)

Primarily businesses interested in sentiment analysis (typically companies involved in advertising, market research, PR, etc.)

Industry/Entity Type

It Company

Requirements
Must have
• We are looking for a clean, modern, and professional design. This includes a logo, homepage, and internal page if it will differ from the homepage.
Nice to have
• It would be excellent if you could provide an HTML mockup if your design is chosen.
Should not have
• Flash, excessive bells and whistles

```html
<!DOCTYPE html>
<html lang="en">
<head>
<meta charset="utf-8">
<title>VantroLux – What we're all about</title>
<link rel="stylesheet" href="https://fonts.googleapis.com/css2?family=Arimo:wght@400;700&family=Francois+One&family=Noto+Sans:wght@400;700&display=swap">
<style>
:root{
  --page-black:#050505;
  --nav-edge:#3a3a3a;
  --panel-white:#ffffff;
  --ink:#111111;
  --link-blue:#9fd4f2;
  --logo-blue:#2b6a9b;
  --footer-bar:#1d1d1d;
  --icon-orange-top:#f7a04a;
  --icon-orange-bottom:#d55f12;
  --icon-red-top:#ef4a2a;
  --icon-red-bottom:#b51c14;
  --icon-grey-top:#5a5a5a;
  --icon-grey-bottom:#262626;
}
*{margin:0;padding:0;box-sizing:border-box}
html,body{width:1200px;height:1200px;overflow:hidden;background:var(--page-black)}
body{position:relative;font-family:"Noto Sans",Verdana,sans-serif;color:var(--ink)}
.canvas{position:absolute;inset:0;background:
  radial-gradient(ellipse 700px 260px at 300px 120px,#3a3a3a 0%,rgba(0,0,0,0) 70%),
  linear-gradient(#1b1b1b 0,#050505 360px,#050505 100%)}
.team-photo{position:absolute;left:0;top:0;width:330px;height:235px;
  background:radial-gradient(ellipse at 45% 40%,#8a7a6a 0%,#4a4038 45%,rgba(20,20,20,0) 80%)}
.tagline{position:absolute;left:308px;top:128px;font-family:"Francois One",Arial,sans-serif;
  color:#fff;font-size:37px;line-height:40px;letter-spacing:.3px}
.brand-glow{position:absolute;left:905px;top:-30px;width:320px;height:290px;border-radius:50%;
  background:radial-gradient(circle,#e6e6e6 0%,#c4c4c4 30%,rgba(40,40,40,0) 70%)}
.brand-mark{position:absolute;left:960px;top:150px;display:flex;align-items:center;gap:10px}
.brand-mark .dot{width:22px;height:22px;border-radius:50%;background:var(--logo-blue)}
.brand-mark .name{font-family:"Arimo",Arial,sans-serif;font-weight:700;font-size:32px;line-height:34px;color:var(--logo-blue)}
.main-nav{position:absolute;left:30px;top:228px;width:1135px;height:118px;border-radius:10px;
  background:linear-gradient(#0c0c0c,#1e1e1e 70%,#2a2a2a);border-bottom:2px solid var(--nav-edge)}
.nav-item{position:absolute;top:14px;display:flex;align-items:center;gap:14px;
  font-family:"Arimo",Arial,sans-serif;font-weight:700;font-size:16px;line-height:18px;color:#fff;text-transform:uppercase}
.nav-icon{width:66px;height:84px;border-radius:8px;display:block}
.icon-orange{background:linear-gradient(var(--icon-orange-top),var(--icon-orange-bottom))}
.icon-red{background:linear-gradient(var(--icon-red-top),var(--icon-red-bottom))}
.icon-grey{background:linear-gradient(var(--icon-grey-top),var(--icon-grey-bottom))}
.content-panel{position:absolute;left:36px;top:363px;width:1131px;height:720px;border-radius:27px;background:var(--panel-white)}
.col{position:absolute;top:0}
.col h2{font-family:"Arimo",Arial,sans-serif;font-weight:700;font-size:26px;line-height:29px;color:var(--ink)}
.col p{font-size:13px;line-height:16.5px;margin-top:14px}
.col-left{left:18px;width:340px;top:22px}
.col-mid{left:422px;width:330px;top:211px}
.col-right{left:794px;width:330px;top:14px}
.board-photo{width:340px;height:219px;margin-top:14px;background:linear-gradient(135deg,#b98a58,#8c6238 60%,#d8d2c8)}
.hero-photo{position:absolute;left:398px;top:9px;width:351px;height:194px;
  background:linear-gradient(110deg,#6d7f9a,#4a5a72 45%,#a58b7c 70%,#3e4a5a);box-shadow:0 5px 8px rgba(0,0,0,.45)}
.col-mid h2{font-size:25px;line-height:29px}
.steps p{margin-top:14px}
.footer-bar{position:absolute;left:42px;top:1114px;width:1128px;height:65px;border-radius:8px;background:var(--footer-bar)}
.footer-links{position:absolute;left:76px;top:25px;display:flex;gap:24px;list-style:none}
.footer-links a{font-size:13px;color:var(--link-blue);text-decoration:underline;font-family:"Arimo",Arial,sans-serif}
.social{position:absolute;left:752px;top:14px;display:flex;gap:21px}
.social span{width:40px;height:40px;border-radius:6px;display:block}
</style>
</head>
<body>
<div class="canvas">
  <div class="team-photo" role="img" aria-label="Photo of a team working together at a laptop"></div>
  <div class="tagline">What we’re<br>all about</div>
  <div class="brand-glow"></div>
  <div class="brand-mark"><span class="dot"></span><span class="name">VantroLux</span></div>

  <nav class="main-nav">
    <div class="nav-item" style="left:80px"><span class="nav-icon icon-orange" role="img" aria-label="Clipboard with pie chart icon"></span>Products<br>&amp; Services</div>
    <div class="nav-item" style="left:295px"><span class="nav-icon icon-orange" role="img" aria-label="Signboard with world map icon"></span>About<br>VantroLux</div>
    <div class="nav-item" style="left:525px"><span class="nav-icon icon-orange" role="img" aria-label="Computer monitor icon"></span>VantroLux<br>Demo</div>
    <div class="nav-item" style="left:760px"><span class="nav-icon icon-grey" role="img" aria-label="Person with headset icon"></span>Our<br>Team</div>
    <div class="nav-item" style="left:925px"><span class="nav-icon icon-red" role="img" aria-label="Circular arrows icon"></span>Let’s<br>Talk</div>
  </nav>

  <main class="content-panel">
    <section class="col col-left">
      <h2>Did we really think we could make a difference?</h2>
      <p><b>Duis autem vel eum</b> iriure dolor in hendrerit in vulputate velit esse molestie consequat, vel illum dolore eu feugiat nulla facilisis at vero eros et accumsan et iusto odio dignissim qui blandit praesent luptatum zzril delenit augue duis dolore te feugait nulla facilisi. Lorem ipsum dolor sit amet, consectetuer adipiscing elit, sed diam nonummy nibh euismod tincidunt ut laoreet dolore magna aliquam erat volutpat.</p>
      <div class="board-photo" role="img" aria-label="Corkboard with pinned team photos and a note"></div>
      <p style="margin-top:6px">Tation ullamcorper suscipit lobortis nisl ut aliquip ex ea commodo consequat. Duis autem vel eum iriure dolor in hendrerit in vulputate velit esse molestie consequat, vel illum dolore eu feugiat nulla facilisis at vero eros et accumsan et iusto odio dignissim qui blandit praesent luptatum zzril delenit augue duis dolore te feugait nulla facilisi.</p>
      <p>Nam liber tempor cum soluta nobis eleifend option congue nihil imperdiet doming id quod mazim placerat facer possim assum. Lorem ipsum dolor sit amet, consectetuer adipiscing elit, sed diam nonummy nibh euismod tincidunt ut laoreet dolore magna aliquam erat volutpat. Ut wisi enim ad</p>
    </section>

    <div class="hero-photo" role="img" aria-label="Collage of a person smiling over a web page background"></div>
    <section class="col col-mid">
      <h2>We take the confusion out of technology and make sense of the online world.</h2>
      <p><b>There are over 13 billion websites</b> in vulputate velit esse molestie consequat, vel illum dolore eu feugiat nulla facilisis at vero eros et accumsan et iusto odio dignissim qui blandit praesent luptatum zzril delenit augue duis dolore te feugait nulla facilisi. Lorem ipsum dolor sit amet, consectetuer adipiscing elit, sed diam nonummy nibh euismod tincidunt ut laoreet dolore magna aliquam erat volutpat.</p>
      <p><b>It is no coincidence</b> veniam, quis nostrud exerci tation ullamcorper suscipit lobortis nisl ut aliquip ex ea commodo consequat. Duis autem vel eum iriure dolor in hendrerit in vulputate velit esse molestie consequat.</p>
      <p>Nam liber tempor cum soluta nobis eleifend option congue nihil imperdiet doming id quod mazim placerat facer possim assum. Lorem ipsum dolor sit amet, consectetuer adipiscing elit, sed diam nonummy nibh euismod tincidunt ut laoreet dolore magna aliquam erat volutpat. Ut wisi enim ad minim v suscipit lobortis nisl ut aliquip ex ea commodo consequat.</p>
    </section>

    <section class="col col-right steps">
      <h2>Ten Web Activities We Learned The Hard Way!</h2>
      <p><b>1)</b> Duis autem vel eum iriure dolor in hendrerit in vulputate velit esse molestie consequat.</p>
      <p><b>2)</b> vel illum dolore eu feugiat nulla facilisis at vero eros et accumsan et iusto odio dignissim qui blandit praesent luptatum zzril delenit</p>
      <p><b>3)</b> Augue duis dolore te feugait nulla facilisi. Lorem ipsum dolor sit amet, consectetuer adipiscing elit, sed diam nonummy nibh.</p>
      <p><b>4)</b> Fuismod tincidunt ut laoreet dolore magna aliquam erat volutpat.</p>
      <p><b>5)</b> Ut wisi enim ad minim veniam, quis nostrud exerci tation ullamcorper suscipit lobortis nisaliquip ex ea commodo consequat.</p>
      <p><b>6)</b> Duis autem vel eum iriure dolor in hendrerit in vulputate velit esse molestie consequat, vel illum dolore eu feugiat nulla</p>
      <p><b>7)</b> Eros et accumsan et iusto odio dignissim qui blandit praesent luptatum zzril delenit.</p>
      <p><b>8)</b> Nam liber tempor cum soluta nobis eleifend option congue nihil imperdiet doming id quod mazim placerat facer possim assum.</p>
      <p><b>9)</b> Lorem ipsum dolor sit amet, consectetuer adipiscing elit, sed diam nonummy nibh euismod tincidunt ut laoreet dolore magna aliquam erat volutpat.</p>
      <p><b>10)</b> Ut wisi enim ad minim veniam, quis nostrud exerci tation ullamcorper suscipit</p>
    </section>
  </main>

  <footer class="footer-bar">
    <ul class="footer-links">
      <li><a href="#">HOME</a></li>
      <li><a href="#">PRODUCTS/SERVICES</a></li>
      <li><a href="#">ABOUS US</a></li>
      <li><a href="#">VANTROLUX DEMO</a></li>
      <li><a href="#">OUR TEAM</a></li>
      <li><a href="#">CONTACT US</a></li>
    </ul>
    <div class="social">
      <span style="background:#2d5fa8"></span>
      <span style="background:#3fa3c9"></span>
      <span style="background:#2e6aa3"></span>
      <span style="background:#5a4a9a"></span>
      <span style="background:#d8d8d8"></span>
    </div>
  </footer>
</div>
</body>
</html>
```